Plumbing business card and logo desgin

Need a new business card and logo for a plumbing business based in Warragul, Australia. Business name is 7Kelby plumbing & air-conditioning. We service all plumbing and gasfitting needs and installation of air-conditioning. We clear blocked drains, install new hot water systems, central heating, new and existing homes, roofing, sanitary and drainage.
i would like to have a space on there for website, email, phone, licence number and what we do as a company.
i would like a water droplet to be incorporated into the design to try and stand out that we are a plumbing business

Contact Information for Business Card

website:
phone number: 0458271936
Licence Number: 382716

Logo Text

7Kelby Plumbing & Air-Conditioning

```html
<!DOCTYPE html>
<html lang="en">
<head>
<meta charset="UTF-8">
<title>7Kelby Plumbing &amp; Air-Conditioning — Business Card</title>
<link rel="stylesheet" href="https://fonts.googleapis.com/css2?family=Arimo:wght@400;700&family=Montserrat:wght@900&display=swap">
<style>
  :root {
    --stage: #262626;
    --blue-light: #23a6e0;
    --blue-deep: #1577c4;
    --white: #ffffff;
    --grey-arc: #a4a5ab;
    --ink-blue: #1e8fd6;
  }
  * { box-sizing: border-box; margin: 0; padding: 0; }
  html, body {
    width: 1200px; height: 1015px; overflow: hidden;
    background: var(--stage);
    font-family: "Arimo", Arial, sans-serif;
  }
  .canvas { position: relative; width: 1200px; height: 1015px; }
  .card {
    position: absolute; left: 280px; width: 640px; height: 366px;
    overflow: hidden;
    background: linear-gradient(160deg, var(--blue-light) 0%, var(--blue-deep) 100%);
    box-shadow: 0 18px 40px rgba(0,0,0,.55);
    color: var(--white);
  }
  .card--services { top: 95px; }
  .card--contact { top: 545px; }

  /* services side */
  .brand {
    position: absolute; left: 0; right: 0; top: 78px;
    display: flex; align-items: center; justify-content: center; gap: 16px;
  }
  .brand__dot {
    width: 38px; height: 38px; border-radius: 50%;
    border: 4px solid var(--white); flex: none;
  }
  .brand__name { font-weight: 700; font-size: 30px; letter-spacing: .5px; line-height: 1.05; }
  .services {
    position: absolute; left: 0; right: 0; top: 180px;
    text-align: center; font-size: 19px; line-height: 26px;
  }
  .services .sep { display: inline-block; margin: 0 6px; }

  /* contact side */
  .circle-art { position: absolute; inset: 0; }
  .brand--contact {
    position: absolute; left: 395px; top: 62px; width: 230px;
    color: var(--ink-blue);
    font-weight: 700; font-size: 23px; line-height: 1.15; text-align: center;
  }
  .brand--contact .brand__dot {
    display: block; margin: 0 auto 14px; width: 54px; height: 54px;
    border-color: var(--ink-blue);
  }
  .person { position: absolute; left: 50px; top: 96px; }
  .person__name {
    font-family: "Montserrat", Arial, sans-serif; font-weight: 900;
    font-size: 26px; letter-spacing: .5px; line-height: 1.1;
  }
  .person__role { font-size: 13px; letter-spacing: 1px; margin-top: 2px; }
  .contacts { list-style: none; margin-top: 20px; font-size: 14px; letter-spacing: .5px; }
  .contacts li { display: flex; align-items: center; gap: 9px; height: 22px; white-space: nowrap; }
  .contacts svg { width: 14px; height: 14px; flex: none; }
  .divider { width: 290px; height: 1px; background: rgba(255,255,255,.7); margin: 16px 0 14px; }
  .licence { font-size: 17px; letter-spacing: .8px; white-space: nowrap; }
</style>
</head>
<body>
<main class="canvas">

  <section class="card card--services" aria-label="Card back: services">
    <div class="brand">
      <span class="brand__dot"></span>
      <span class="brand__name">7Kelby Plumbing &amp;<br>Air-Conditioning</span>
    </div>
    <p class="services">
      All plumbing<span class="sep">•</span>Gasfitting<span class="sep">•</span>Installation of air-conditioning<br>
      Clear blocked drains<span class="sep">•</span>Install new hot water systems<br>
      Central Heating<span class="sep">•</span>New and Existing homes<br>
      Roofing<span class="sep">•</span>Sanitary and Drainage
    </p>
  </section>

  <section class="card card--contact" aria-label="Card front: contact details">
    <svg class="circle-art" viewBox="0 0 640 366" aria-hidden="true">
      <circle cx="548" cy="94" r="206" fill="var(--grey-arc)"/>
      <circle cx="558" cy="88" r="200" fill="var(--white)"/>
    </svg>

    <div class="brand--contact">
      <span class="brand__dot"></span>
      7Kelby Plumbing &amp;<br>Air-Conditioning
    </div>

    <div class="person">
      <h1 class="person__name">RYAN KELBY</h1>
      <p class="person__role">MANAGING DIRECTOR</p>
      <ul class="contacts">
        <li>
          <svg viewBox="0 0 24 24"><path fill="#fff" d="M6.6 10.8a15 15 0 0 0 6.6 6.6l2.2-2.2c.3-.3.7-.4 1-.2 1.1.4 2.3.6 3.6.6.6 0 1 .4 1 1V20c0 .6-.4 1-1 1A17 17 0 0 1 3 4c0-.6.4-1 1-1h3.5c.6 0 1 .4 1 1 0 1.3.2 2.5.6 3.6.1.3 0 .7-.2 1z"/></svg>
          0458271936
        </li>
        <li>
          <svg viewBox="0 0 24 24"><path fill="#fff" d="M2 5h20v14H2z"/><path fill="none" stroke="#1a86cd" stroke-width="1.8" d="M2 5l10 8 10-8"/></svg>
          INFO@7KELBYPLUMBING.COM
        </li>
        <li>
          <svg viewBox="0 0 24 24" fill="none" stroke="#fff" stroke-width="1.8"><circle cx="12" cy="12" r="9.5"/><path d="M2.5 12h19M12 2.5c3 3 3 16 0 19M12 2.5c-3 3-3 16 0 19"/></svg>
          WWW.7KELBYPLUMBING.COM
        </li>
      </ul>
      <div class="divider"></div>
      <p class="licence">LICENCE NUMBER: 382716</p>
    </div>
  </section>

</main>
</body>
</html>
```